Design powerpoint slide template

Hello,
I need help with designing a template for a powerpoint presentation for a new startup.

I am attaching a sample slide (with lorem ipsum text) from our pitch deck, as well as our company logo.

Requirements:
- elegant
- modern
- not using many colours (e.g. black, white and red - not a rainbow...)
- including page number (somewhere)

THE PERSON WHO WINS THIS CONTEST WILL RECEIVE A FOLLOW-UP JOB - to modify the pitch deck (12 slides) using the template (as well as to create new designs/icons etc. as required for the other slides). Price to be negotiated.

Thank you for your help!

```html
<!DOCTYPE html>
<html lang="en">
<head>
<meta charset="utf-8">
<title>Kestrel – Slide Template</title>
<link href="https://fonts.googleapis.com/css2?family=Montserrat:wght@400;600;700&family=Oswald:wght@500;700&family=Archivo+Black&display=swap" rel="stylesheet">
<style>
:root{
  --red:#e0281e;
  --red-dark:#a91c14;
  --ink:#2b2b2b;
  --panel:#3a3a3a;
  --photo-top:#4a4a4a;
  --photo-bottom:#161616;
  --paper:#ffffff;
  --stage:#ececec;
  --muted:#555;
}
*{box-sizing:border-box;margin:0;padding:0}
html,body{width:1200px;height:1040px;overflow:hidden}
body{background:var(--stage);font-family:"Montserrat",sans-serif;position:relative;color:var(--ink)}
.slide{position:absolute;width:540px;height:305px;background:var(--paper);overflow:hidden;box-shadow:0 2px 6px rgba(0,0,0,.25)}
.slide svg.bg{position:absolute;inset:0;width:100%;height:100%}
.slide--cover{left:40px;top:47px}
.slide--swot{left:616px;top:47px}
.slide--problem-a{left:40px;top:376px}
.slide--thanks{left:616px;top:376px}
.slide--problem-b{left:40px;top:703px}
.abs{position:absolute}
.brand{font-family:"Montserrat",sans-serif;font-weight:700;color:var(--red);letter-spacing:.18em}
.brand--small{font-size:10px;left:20px;top:14px}
.brand--large{font-size:38px;left:30px;top:236px;letter-spacing:.16em}
.cover-meta{right:26px;top:262px;font-size:8px;font-weight:600;color:var(--ink);letter-spacing:.03em}
.page-no{width:13px;height:13px;background:var(--red);color:#fff;font-size:6.5px;font-weight:700;display:flex;align-items:center;justify-content:center}
.swot-title{left:146px;top:28px;font-size:9.5px;font-weight:700;color:var(--red);white-space:nowrap}
.swot-col{top:86px;width:75px;color:#fff;font-size:5.6px;line-height:1.35;padding:0 8px 0 10px}
.swot-col ol{padding-left:8px}
.swot-col li{margin-bottom:6px}
.swot-col strong{font-weight:600}
.swot-letter{width:68px;text-align:center;font-family:"Oswald",sans-serif;font-weight:700;color:var(--ink);font-size:36px;line-height:1;top:212px}
.swot-label{width:68px;text-align:center;font-size:5.5px;font-weight:700;color:var(--red);top:256px}
.vertical-title{font-family:"Oswald",sans-serif;font-weight:500;font-size:26px;letter-spacing:.18em;color:#fff;transform:rotate(-90deg);transform-origin:center;white-space:nowrap}
.hub-text{text-align:center;font-family:"Oswald",sans-serif;font-weight:500;color:var(--ink);line-height:1.05}
.point{left:228px;width:220px;text-align:center}
.point h3{font-family:"Oswald",sans-serif;font-weight:500;font-size:10px;color:var(--red-dark);line-height:1.15;letter-spacing:.02em}
.point p{font-size:6.5px;color:var(--ink);line-height:1.35;margin-top:2px}
.thanks-title{right:36px;top:56px;font-family:"Archivo Black",sans-serif;font-size:21px;color:var(--red);letter-spacing:.01em}
.side-copy{left:12px;top:130px;width:108px;text-align:right;font-size:8px;line-height:1.4;color:var(--ink)}
.side-copy small{display:block;font-size:6px;font-weight:700}
.node-copy{width:110px;text-align:center;font-size:6.3px;line-height:1.35;color:#ddd;top:218px}
</style>
</head>
<body>

<!-- Cover -->
<section class="slide slide--cover">
  <svg class="bg" viewBox="0 0 540 305" role="img" aria-label="Dark photograph of water droplets on a black surface">
    <defs>
      <linearGradient id="photo1" x1="0" y1="0" x2="1" y2="1">
        <stop offset="0" stop-color="var(--photo-top)"/>
        <stop offset="1" stop-color="var(--photo-bottom)"/>
      </linearGradient>
    </defs>
    <rect width="540" height="305" fill="url(#photo1)"/>
    <polygon points="0,205 540,178 540,305 0,305" fill="var(--paper)"/>
    <polygon points="250,208 540,152 540,178 300,205" fill="var(--red)"/>
    <polygon points="180,305 540,262 540,272 260,305" fill="var(--red)"/>
    <polygon points="260,305 540,272 540,305" fill="var(--ink)"/>
  </svg>
  <div class="abs brand brand--large">KESTREL</div>
  <div class="abs cover-meta">COMPANY PROFILE &nbsp;|&nbsp; 2017</div>
</section>

<!-- SWOT -->
<section class="slide slide--swot">
  <svg class="bg" viewBox="0 0 540 305">
    <defs>
      <linearGradient id="colShade" x1="0" y1="0" x2="0" y2="1">
        <stop offset="0" stop-color="#e33a2c"/>
        <stop offset="1" stop-color="#b8211a"/>
      </linearGradient>
      <linearGradient id="titleBar" x1="0" y1="0" x2="0" y2="1">
        <stop offset="0" stop-color="#fafafa"/>
        <stop offset="1" stop-color="#dcdcdc"/>
      </linearGradient>
    </defs>
    <rect x="138" y="24" width="172" height="26" fill="url(#titleBar)"/>
    <rect x="306" y="24" width="4" height="26" fill="var(--red)"/>
    <circle cx="120" cy="40" r="22" fill="none" stroke="var(--red)" stroke-width="4" stroke-dasharray="110 40"/>
    <circle cx="120" cy="40" r="16" fill="var(--red)"/>
    <text x="120" y="38" text-anchor="middle" font-family="Oswald" font-weight="700" font-size="8" fill="#fff">SW</text>
    <text x="122" y="47" text-anchor="middle" font-family="Oswald" font-weight="700" font-size="8" fill="#fff">OT</text>
    <rect x="50" y="112" width="16" height="193" fill="var(--panel)"/>
    <rect x="137" y="78" width="75" height="160" fill="url(#colShade)"/>
    <rect x="212" y="78" width="75" height="160" fill="#d72c20"/>
    <rect x="287" y="78" width="75" height="160" fill="url(#colShade)"/>
    <rect x="362" y="78" width="75" height="160" fill="#d72c20"/>
    <g fill="#fff" stroke="var(--red)" stroke-width="3">
      <circle cx="174.5" cy="240" r="35"/>
      <circle cx="249.5" cy="240" r="35"/>
      <circle cx="324.5" cy="240" r="35"/>
      <circle cx="399.5" cy="240" r="35"/>
    </g>
    <g fill="none" stroke="#e6e6e6" stroke-width="1">
      <circle cx="174.5" cy="240" r="29"/>
      <circle cx="249.5" cy="240" r="29"/>
      <circle cx="324.5" cy="240" r="29"/>
      <circle cx="399.5" cy="240" r="29"/>
    </g>
  </svg>
  <div class="abs brand brand--small">KESTREL</div>
  <div class="abs page-no" style="right:20px;top:14px">02</div>
  <div class="abs swot-title">SWOT ANALYSIS of KESTREL</div>
  <div class="abs swot-col" style="left:137px"><ol><li>Nunc sit amet libero egestas mattis mi nec. Morbi eu mauris placerat, ultrices neque et, laoreet lorem.</li><li><strong>Proin id Risus posuere ipsum tristiqu</strong></li></ol></div>
  <div class="abs swot-col" style="left:212px"><ol><li>Nunc sit amet libero egestas mattis mi nec. Morbi eu mauris placerat, ultrices neque et, laoreet lorem.</li><li><strong>Proin id Risus posuere ipsum tristiqu</strong></li></ol></div>
  <div class="abs swot-col" style="left:287px"><ol><li>Nunc sit amet libero egestas mattis mi nec. Morbi eu mauris placerat, ultrices neque et, laoreet lorem.</li><li><strong>Proin id Risus posuere ipsum tristiqu</strong></li></ol></div>
  <div class="abs swot-col" style="left:362px"><ol><li>Nunc sit amet libero egestas mattis mi nec. Morbi eu mauris placerat, ultrices neque et, laoreet lorem.</li><li><strong>Proin id Risus posuere ipsum tristiqu</strong></li></ol></div>
  <div class="abs swot-letter" style="left:140.5px">S</div>
  <div class="abs swot-letter" style="left:215.5px">W</div>
  <div class="abs swot-letter" style="left:290.5px">O</div>
  <div class="abs swot-letter" style="left:365.5px">T</div>
  <div class="abs swot-label" style="left:140.5px">STRENGTH</div>
  <div class="abs swot-label" style="left:215.5px">WEAKNESS</div>
  <div class="abs swot-label" style="left:290.5px">OPPORTUNITY</div>
  <div class="abs swot-label" style="left:365.5px">THREAT</div>
</section>

<!-- Problem 01 -->
<section class="slide slide--problem-a">
  <svg class="bg" viewBox="0 0 540 305">
    <rect x="467" y="0" width="73" height="305" fill="var(--panel)"/>
    <g fill="var(--red-dark)">
      <path d="M152.6,18.3 A128,128 0 0 1 226,80 L171.3,109 A66,66 0 0 0 133.4,77.2 Z"/>
      <path d="M231.7,92 A128,128 0 0 1 231.7,188 L174.2,164.7 A66,66 0 0 0 174.2,115.3 Z" fill="var(--red)"/>
      <path d="M226,200 A128,128 0 0 1 152.6,261.7 L133.4,202.8 A66,66 0 0 0 171.3,171 Z"/>
    </g>
    <rect x="111" y="190" width="4" height="86" fill="var(--red-dark)"/>
    <circle cx="113" cy="278" r="7" fill="#d9d9d9"/>
    <circle cx="113" cy="278" r="4" fill="var(--red-dark)"/>
    <circle cx="113" cy="140" r="60" fill="var(--red)"/>
    <circle cx="113" cy="140" r="45" fill="#fff"/>
    <circle cx="113" cy="140" r="45" fill="none" stroke="#e0e0e0" stroke-width="2"/>
  </svg>
  <div class="abs brand brand--small">KESTREL</div>
  <div class="abs page-no" style="right:20px;top:14px">01</div>
  <div class="abs vertical-title" style="left:445px;top:138px;width:120px;text-align:center">PROBLEM</div>
  <div class="abs hub-text" style="left:68px;top:116px;width:90px">
    <div style="font-size:9px">SUSPENDISSE</div>
    <div style="font-size:12px;font-weight:700">SAGITTIS</div>
    <div style="font-size:9px">AUGUE VEL</div>
    <div style="font-size:5.5px;font-family:Montserrat,sans-serif;font-weight:700">(LOREM IPSUM 1.0)</div>
  </div>
  <div class="abs point" style="top:52px"><h3>AENEAN PHARETRA VULPUTATE EXHIGH<br>COST OF BANKING SERVICES</h3><p>Sed luctus non orci vitae ornare. Vestibulum<br>risus nulla, tristique a aliquam id, ultrices non elit</p></div>
  <div class="abs point" style="top:130px"><h3>NUNC NON VIVERRA NULLA</h3><p>Quisque ac tellus quis augue<br>luctus aliquam ac id diam.</p></div>
  <div class="abs point" style="top:210px"><h3>QUISQUE AC TELLUS QUIS<br>AUGUE LUCTUS</h3><p>Liiquam vel ex est. Nullam hendrerit<br>ac tortor a varius. Sed ultricies, dui at sagittis<br>luctus, mauris nunc commodo odio.</p></div>
</section>

<!-- Thank you -->
<section class="slide slide--thanks">
  <svg class="bg" viewBox="0 0 540 305" role="img" aria-label="Dark photograph of water droplets on a black surface">
    <defs>
      <linearGradient id="photo2" x1="0" y1="0" x2="1" y2="1">
        <stop offset="0" stop-color="var(--photo-top)"/>
        <stop offset="1" stop-color="var(--photo-bottom)"/>
      </linearGradient>
    </defs>
    <rect width="540" height="305" fill="url(#photo2)"/>
    <polygon points="0,62 190,0 540,0 540,88 0,118" fill="var(--paper)"/>
    <polygon points="140,18 190,0 410,0" fill="var(--red)"/>
    <polygon points="0,118 540,88 540,92 0,140" fill="var(--red)"/>
  </svg>
  <div class="abs thanks-title">THANK YOU</div>
</section>

<!-- Problem 02 -->
<section class="slide slide--problem-b">
  <svg class="bg" viewBox="0 0 540 305">
    <rect x="130" y="0" width="410" height="305" fill="var(--panel)"/>
    <path d="M247,38 A52,52 0 1 1 195,90" fill="none" stroke="var(--red)" stroke-width="14"/>
    <path d="M363,45 A52,52 0 0 1 415,97" fill="none" stroke="var(--red)" stroke-width="14"/>
    <path d="M300,97 A63,63 0 0 1 363,34" fill="none" stroke="var(--red-dark)" stroke-width="4"/>
    <rect x="245" y="120" width="3" height="84" fill="var(--red)"/>
    <rect x="361" y="127" width="3" height="77" fill="var(--red)"/>
    <rect x="172" y="200" width="282" height="9" rx="4.5" fill="#f2f2f2"/>
    <circle cx="246.5" cy="204.5" r="5" fill="var(--red)"/>
    <circle cx="362.5" cy="204.5" r="5" fill="var(--panel)"/>
    <circle cx="247" cy="90" r="38" fill="#fff"/>
    <circle cx="363" cy="97" r="38" fill="#fff"/>
    <circle cx="247" cy="90" r="38" fill="none" stroke="#dcdcdc" stroke-width="3"/>
    <circle cx="363" cy="97" r="38" fill="none" stroke="#dcdcdc" stroke-width="3"/>
  </svg>
  <div class="abs brand brand--small">KESTREL</div>
  <div class="abs page-no" style="right:20px;top:14px">02</div>
  <div class="abs vertical-title" style="left:440px;top:138px;width:120px;text-align:center">PROBLEM</div>
  <div class="abs side-copy">Proin Id Risus<br>Posuere Ipsum<br>Tristique Lacinia<br>In Eget Libero<br>Ut Commodo<small>(LOREM IPSUM 2.0)</small></div>
  <div class="abs hub-text" style="left:212px;top:70px;width:70px">
    <div style="font-size:9.5px;font-weight:700">VIVAMUS IN</div>
    <div style="font-size:7px">NULLA AC NIBH</div>
    <div style="font-size:6px">ELEIFEND ALIQUAM</div>
    <div style="font-size:9.5px;font-weight:700">A VEL EST</div>
  </div>
  <div class="abs hub-text" style="left:328px;top:79px;width:70px">
    <div style="font-size:11px;font-weight:700">PROIN ID</div>
    <div style="font-size:7px">RISUS POSUERE</div>
    <div style="font-size:7px">IPSUM TRISTIQU</div>
  </div>
  <div class="abs node-copy" style="left:191px">Nunc sit amet libero egestas mattis mi nec, placerat ex. Morbi eu mauris placerat, ultrices neque et, laoreet lorem.</div>
  <div class="abs node-copy" style="left:308px">Nunc sit amet libero egestas mattis mi nec, placerat ex. Morbi eu mauris placerat, ultrices neque et, laoreet lorem.</div>
</section>

</body>
</html>
```